Youtube Graphic Design for Fitness Brand

I own a personal training/fitness brand called Bright Quarry Fitness. I am starting my YouTube channel and need artwork for my banner and an animated intro/outro. For my banner, I would like to see designs that incorporate my brand logo and one of the attached images of me. The point of my channel is to help educate others and help them achieve their fitness goals to live happy balanced lives. The final design should present a high quality fitness brand that offers value to its subscribers. I'd like to keep the project with either a predominately black or white color. Not sure if I have a preference on either color being the dominant color.

Target Market(s)

People looking for help with fitness/healthy lifestyle.

Industry/Entity Type

Fitness

Requirements
Must have
• My logo
Nice to have
• One of the attached photos of me

```html
<!DOCTYPE html>
<html lang="en">
<head>
<meta charset="utf-8">
<title>Bright Quarry Fitness – Channel Banner</title>
<link href="https://fonts.googleapis.com/css2?family=Kanit:ital,wght@1,800&family=Open+Sans:wght@300;600&display=swap" rel="stylesheet">
<style>
  :root {
    --navy: #18114f;
    --white: #ffffff;
    --ring-white: #f6f3f8;
    --ink: #111111;
    --photo-dark: #2a2630;
    --photo-warm: #b98a78;
  }
  * { margin: 0; padding: 0; box-sizing: border-box; }
  html, body { width: 1200px; height: 675px; overflow: hidden; background: var(--navy); }
  .banner {
    position: relative; width: 1200px; height: 675px;
    background: var(--navy); color: var(--white); overflow: hidden;
    font-family: "Open Sans", sans-serif;
  }
  .deco { position: absolute; display: block; }
  .dots-left { left: 60px; top: 209px; }
  .chevrons-up { left: 60px; top: 434px; }
  .chevrons-down { left: 1119px; top: 209px; }
  .dots-right { left: 1127px; top: 413px; }

  .channel-title {
    position: absolute; left: 144px; top: 288px;
    font-family: "Kanit", sans-serif; font-weight: 800; font-style: italic;
    font-size: 45px; line-height: 46px; letter-spacing: 5px;
    text-transform: uppercase;
  }
  .channel-title span { display: block; }
  .channel-title .line-one { padding-left: 11px; }

  .brand-tile {
    position: absolute; left: 153px; top: 410px; width: 96px; height: 63px;
    background: var(--white); color: var(--ink);
    display: flex; flex-direction: column; align-items: center; justify-content: center; gap: 4px;
  }
  .brand-tile .mark { width: 18px; height: 18px; border-radius: 50%; background: var(--ink); }
  .brand-tile .name {
    font-family: "Open Sans", sans-serif; font-weight: 600;
    font-size: 7px; letter-spacing: 0.6px; text-transform: uppercase; text-align: center; line-height: 9px;
  }

  .portrait-rings { position: absolute; left: 465px; top: 202px; }

  .subscribe-cta { position: absolute; left: 820px; top: 275px; width: 230px; height: 90px; }
  .subscribe-cta svg { position: absolute; left: 0; top: 0; }
  .subscribe-text {
    position: absolute; left: 0; top: 4px; width: 212px; text-align: center;
    font-family: "Kanit", sans-serif; font-weight: 800; font-style: italic;
    font-size: 28px; line-height: 33px; letter-spacing: 3px; text-transform: uppercase;
  }
  .tagline {
    position: absolute; right: 171px; top: 352px; text-align: right;
    font-weight: 300; font-size: 15px; line-height: 22px; letter-spacing: 1.6px;
    text-transform: uppercase;
  }
</style>
</head>
<body>
<main class="banner">
  <svg class="deco dots-left" width="14" height="56" viewBox="0 0 14 56" aria-hidden="true">
    <circle cx="7" cy="6" r="6.3" fill="#fff"/><circle cx="7" cy="26.5" r="6.3" fill="#fff"/><circle cx="7" cy="47" r="6.3" fill="#fff"/>
  </svg>
  <svg class="deco chevrons-up" width="22" height="34" viewBox="0 0 22 34" aria-hidden="true">
    <g fill="none" stroke="#fff" stroke-width="2.4">
      <polyline points="1,11 11,2 21,11"/><polyline points="1,21 11,12 21,21"/><polyline points="1,31 11,22 21,31"/>
    </g>
  </svg>
  <svg class="deco chevrons-down" width="22" height="34" viewBox="0 0 22 34" aria-hidden="true">
    <g fill="none" stroke="#fff" stroke-width="2.4">
      <polyline points="1,2 11,11 21,2"/><polyline points="1,12 11,21 21,12"/><polyline points="1,22 11,31 21,22"/>
    </g>
  </svg>
  <svg class="deco dots-right" width="14" height="56" viewBox="0 0 14 56" aria-hidden="true">
    <circle cx="7" cy="6" r="6.3" fill="#fff"/><circle cx="7" cy="26.5" r="6.3" fill="#fff"/><circle cx="7" cy="47" r="6.3" fill="#fff"/>
  </svg>

  <h1 class="channel-title"><span class="line-one">Fitness</span><span>Channel</span></h1>

  <div class="brand-tile">
    <span class="mark"></span>
    <span class="name">Bright Quarry<br>Fitness</span>
  </div>

  <svg class="portrait-rings" width="270" height="270" viewBox="0 0 270 270">
    <defs>
      <radialGradient id="photoTone" cx="50%" cy="45%" r="60%">
        <stop offset="0" stop-color="var(--photo-warm)"/>
        <stop offset="0.55" stop-color="#5a4648"/>
        <stop offset="1" stop-color="var(--photo-dark)"/>
      </radialGradient>
    </defs>
    <circle cx="135" cy="135" r="135" fill="var(--ring-white)"/>
    <circle cx="135" cy="135" r="112.5" fill="var(--navy)"/>
    <circle cx="135" cy="135" r="99.5" fill="none" stroke="#fff" stroke-width="0.8"/>
    <circle cx="135" cy="135" r="87" fill="var(--ring-white)"/>
    <circle cx="135" cy="135" r="75.5" fill="url(#photoTone)" role="img" aria-label="Photo of the trainer training with dumbbells in a gym"/>
  </svg>

  <div class="subscribe-cta">
    <svg width="230" height="90" viewBox="0 0 230 90" aria-hidden="true">
      <g fill="none" stroke="#fff" stroke-width="1.2">
        <polyline points="17,33 9,33 9,74 214,74 214,34"/>
        <line x1="190" y1="33" x2="203" y2="33"/>
      </g>
      <circle cx="214" cy="34" r="10.5" fill="#fff"/>
      <g stroke="var(--navy)" stroke-width="1.5">
        <line x1="214" y1="27" x2="214" y2="41"/><line x1="207" y1="34" x2="221" y2="34"/>
      </g>
    </svg>
    <p class="subscribe-text">Subscribe<br>Now!</p>
  </div>

  <p class="tagline">New Routines<br>Every Day</p>
</main>
</body>
</html>
```